Red Kettle Handcrafted Tomato Ketchup packaging design modern

From the best ingredients there is the best ketchup Red Handcrafted ketchup are specially formulated for fine dining and drinks, bringing out all the flavors. As the Red Kettle handcrafted ketchup is otherwise fabulous: Made with wholesome, fully ripe fruits Nothing with half things! All Red Kettle handcrafted ketchups are pure nature, without any artificial diluents or concentrates. Where tomato is on it, that's all there is to it - guaranteed! the design should be professional and noble despite being trendy. A watcher wants to sell the ketchup as merchandising from our restaurant. but as a single brand positioning. The ketchup is vegan. Dimensions: 6.8 cm Height: 7.8 cm Circumference: 21.6 cm The text down (Text 1-4). The lid of the text the glass packaging is black! Thanks for your efforts. I look forward to your designs.

Target Market(s)

foodies

Font styles to use
Serif
Sans Serif

Colors

Designer to choose colors to be used in the design.

Requirements
Must have
• Title: (Handcrafted Tomato Ketchup) Text One: (Store chilled after opening and consume quickly, pasteurized.) Text Two: (Handcrafted in Switzerland by Brentwick Gastro GmbH, Chur www.redkettle-example.ch) Text Tree: (Tomatoes, White Wine Vinegar, Aceto Balsamico, Brown Cane Sugar, Corn Starch, Spices, Salt) Text For: (200 grams) or (200g) The Logo of Red Kettle with the Pasta and Wine have to because of the gesety.
Nice to have
• small vegan icon (maybe)
Should not have
• text of the logo (pasta & wine)

```html
<!DOCTYPE html>
<html lang="de">
<head>
<meta charset="utf-8">
<title>Red Kettle – Handcrafted Tomato Ketchup Label</title>
<link rel="stylesheet" href="https://fonts.googleapis.com/css2?family=Alfa+Slab+One&family=Josefin+Sans:wght@400&family=Arimo:wght@400&display=swap">
<style>
  :root {
    --label-white: #ffffff;
    --label-green: #077d14;
    --ketchup-red: #b0100e;
    --ink: #111111;
    --page: #ececec;
  }
  * { box-sizing: border-box; margin: 0; padding: 0; }
  html, body { width: 1200px; height: 1200px; overflow: hidden; }
  body {
    background: var(--page);
    position: relative;
    font-family: "Arimo", Arial, sans-serif;
    color: var(--ink);
  }
  .label {
    position: absolute;
    top: 400px;
    width: 520px;
    height: 400px;
    background: var(--label-white);
    overflow: hidden;
    box-shadow: 0 2px 10px rgba(0,0,0,.12);
  }
  .label--front { left: 60px; }
  .label--back { left: 620px; }
  .label__wave { position: absolute; inset: 0; width: 100%; height: 100%; }

  .brand-row {
    position: absolute; left: 0; right: 0;
    display: flex; justify-content: center;
  }
  .brand {
    display: inline-block;
    font-family: "Josefin Sans", sans-serif;
    letter-spacing: .22em;
    text-transform: uppercase;
    color: var(--ink);
    white-space: nowrap;
    background: var(--label-white);
    border: 2px solid var(--ink);
    line-height: 1;
  }

  /* front */
  .front__frame { position: absolute; inset: 0; width: 100%; height: 100%; }
  .front__brand-row { top: 78px; }
  .front__brand-row .brand {
    font-size: 24px;
    padding: 12px 10px 9px 16px;
    outline: 1px solid var(--ink);
    outline-offset: -6px;
  }
  .front__title {
    position: absolute; left: 70px; top: 150px; width: 380px;
    transform: rotate(-7deg); transform-origin: center;
    text-align: center;
    white-space: nowrap;
    font-weight: normal;
  }
  .title__handcrafted {
    display: block;
    font-family: "Alfa Slab One", Georgia, serif;
    font-size: 34px;
    color: var(--label-white);
    -webkit-text-stroke: 1.5px var(--ink);
    line-height: 1;
  }
  .title__ketchup {
    display: block;
    margin: 4px -6px 0;
    padding: 7px 0 5px;
    background: var(--ketchup-red);
    font-family: "Alfa Slab One", Georgia, serif;
    font-size: 30px;
    color: var(--label-white);
    line-height: 1;
  }
  .front__vegan {
    position: absolute; left: 402px; top: 312px;
    width: 48px; height: 48px; border-radius: 50%;
    background: var(--label-white);
    border: 2px solid var(--ink);
  }

  /* back */
  .back__brand-row { top: 44px; }
  .back__brand-row .brand {
    font-size: 15px;
    padding: 8px 8px 6px 12px;
    outline: 1px solid var(--ink);
    outline-offset: -5px;
  }
  .back__text {
    position: absolute; left: 48px; right: 30px;
    font-size: 15px; line-height: 1.15; color: var(--ink);
  }
  .back__ingredients { top: 120px; }
  .back__storage { top: 190px; }
  .back__maker { top: 250px; }
  .back__web { top: 300px; }
  .back__weight {
    position: absolute; right: 58px; top: 312px;
    font-size: 19px; color: var(--label-white);
  }
</style>
</head>
<body>

<section class="label label--front" aria-label="Front label">
  <svg class="label__wave" viewBox="0 0 520 400" aria-hidden="true">
    <path d="M0 230 C120 230 200 200 280 175 C360 150 420 225 520 225 L520 400 L0 400 Z" fill="var(--label-green)"/>
  </svg>
  <svg class="front__frame" viewBox="0 0 520 400" aria-hidden="true">
    <rect x="70" y="100" width="380" height="265" fill="none" stroke="#111" stroke-width="2"/>
    <rect x="78" y="108" width="364" height="249" fill="none" stroke="#111" stroke-width="1"/>
  </svg>
  <div class="brand-row front__brand-row"><span class="brand">Red Kettle</span></div>
  <h1 class="front__title">
    <span class="title__handcrafted">HANDCRAFTED</span>
    <span class="title__ketchup">TOMATO KETCHUP</span>
  </h1>
  <div class="front__vegan" role="img" aria-label="Vegan mark"></div>
</section>

<section class="label label--back" aria-label="Back label">
  <svg class="label__wave" viewBox="0 0 520 400" aria-hidden="true">
    <path d="M0 232 C100 232 150 200 220 185 C290 170 330 230 420 232 C470 232 500 228 520 228 L520 400 L0 400 Z" fill="var(--label-green)"/>
  </svg>
  <div class="brand-row back__brand-row"><span class="brand">Red Kettle</span></div>
  <p class="back__text back__ingredients">INGREDIENTS:<br>Tomaten, Weissweinessig, Aceto Balsamico,<br>brauner Rohrzucker, Maisstärke, Gewürze, Salz</p>
  <p class="back__text back__storage">Nach dem Öffnen gekühlt aufbewahren<br>und rasch konsumieren. Pasteurisiert.</p>
  <p class="back__text back__maker">Handcrafted in Switzerland<br>by Brentwick Gastro GmbH, Chur</p>
  <p class="back__text back__web">www.redkettle-example.ch</p>
  <p class="back__weight">200g</p>
</section>

</body>
</html>
```